Tend Your Harvest - Keep your Bloom - The freedom to choose and participate in your own path to hea

I have a logo that needs to be turned into a large banner for my website. I want to keep the same font in the uploaded logo image. Now this image could stay at the top of the header kind of where it is now on the web site, It doesn't have to be the main thing on the page. I want this header to be artistic - alive, healthy, joyous - colorful banner that shows wellness, healing, vitality and hope.
If you had a chronic illness and came to my site what would you want to see? You'd want to feel empowered, enlightened, engaged, hopeful and feel the love, right?.
I look forward to getting your creative ideas and designs.

Target Market(s)

People struggling with illness who are looking for a better quality of life. We provide training and education on how to do that. Hope, happiness - healing - Vitality - whole natural foods - mediation - visualization - whole health.

Industry/Entity Type

Health And Wellness

Logo Text

Tend Your Harvest with the koru and with Marigold Thwaite (use the font on the uploaded file)

Requirements
Must have
• I've changed the photos in this order. You can pick up options here:
• https://www.filebarrow.example/s/x7pleqnrtwz2kdm/IMG_4402%20%20high%20resolution.jpg?dl=0
• https://www.filebarrow.example/s/m3bvohqyeuc8zta/IMG_4587%20high%20resolution.jpg?dl=0
• My original logo - Tend Your Harvest - Marigold Thwaite
• "Together we make tragic moments magic moments" Join us (sign up type button)
Nice to have
• Something stunningly simple, classy, inviting, where my message gets across.
• Here's a similar website to mine: http://dalvenhope.example
• I need a link to join up somewhere - with my quote.
• "My tragic moments have become magic moments" Join us (sign up type button)
Should not have
• I do not want other people in the header.
• No crunchy granola feel!
• This is gone mainstream now.

```html
<!DOCTYPE html>
<html lang="en">
<head>
<meta charset="utf-8">
<title>Tend Your Harvest — Header Banner</title>
<link rel="stylesheet" href="https://fonts.googleapis.com/css2?family=Varela+Round&family=Didact+Gothic&display=swap">
<style>
  :root {
    --teal: #4fb8ad;
    --teal-deep: #2f9489;
    --ink: #2b5a55;
    --orange: #ea5a1c;
    --paper: #ffffff;
    --logo-blue: #3aa9b5;
    --bokeh-gold: #e9c95a;
    --bokeh-rose: #e98a86;
    --bokeh-coral: #f2a072;
    --bokeh-cream: #f6efe6;
  }
  html, body {
    margin: 0;
    padding: 0;
    overflow: hidden;
    background: var(--bokeh-cream);
  }
  .banner {
    position: relative;
    width: 1200px;
    height: 440px;
    overflow: hidden;
  }
  .banner__backdrop {
    position: absolute;
    inset: 0;
    background:
      radial-gradient(ellipse 420px 300px at 360px 40px, rgba(233, 201, 90, 0.85), transparent 70%),
      radial-gradient(ellipse 380px 260px at 520px 380px, rgba(233, 138, 134, 0.85), transparent 70%),
      radial-gradient(ellipse 300px 220px at 760px 300px, rgba(242, 160, 114, 0.6), transparent 70%),
      radial-gradient(ellipse 360px 260px at 930px 150px, rgba(255, 255, 255, 0.95), transparent 70%),
      linear-gradient(100deg, var(--bokeh-gold) 0%, var(--bokeh-coral) 40%, var(--bokeh-rose) 58%, var(--bokeh-cream) 82%);
  }
  .banner__portrait {
    position: absolute;
    left: 0;
    top: 0;
    width: 290px;
    height: 440px;
    background: linear-gradient(180deg, #e8c7a6 0%, #dcb48f 28%, #9fd6d3 45%, #86cbc8 100%);
    -webkit-mask-image: linear-gradient(90deg, #000 80%, transparent 100%);
            mask-image: linear-gradient(90deg, #000 80%, transparent 100%);
  }
  .invite {
    position: absolute;
    left: 272px;
    top: 96px;
    width: 346px;
    display: flex;
    flex-direction: column;
    align-items: center;
    gap: 12px;
    font-family: "Varela Round", sans-serif;
  }
  .invite__kicker {
    margin: 0;
    font-size: 26px;
    color: var(--paper);
    letter-spacing: 0.5px;
  }
  .invite__card {
    box-sizing: border-box;
    width: 100%;
    padding: 20px 18px;
    background: var(--paper);
    border-radius: 4px;
    text-align: center;
  }
  .invite__line {
    margin: 0;
    font-size: 25px;
    line-height: 1.35;
    color: var(--ink);
  }
  .invite__line--accent {
    color: var(--teal-deep);
  }
  .invite__button {
    display: inline-block;
    padding: 9px 34px;
    background: var(--paper);
    border: 2px solid var(--teal);
    border-radius: 24px;
    font-size: 22px;
    color: var(--orange);
    text-decoration: none;
  }
  .brand {
    position: absolute;
    top: 28px;
    right: 44px;
    font-family: "Didact Gothic", sans-serif;
    color: var(--logo-blue);
  }
  .brand__name {
    display: block;
    font-size: 25px;
    line-height: 1.15;
  }
  .brand__person {
    display: flex;
    align-items: center;
    gap: 8px;
    font-size: 22px;
    line-height: 1.25;
  }
  .brand__dot {
    width: 14px;
    height: 14px;
    border-radius: 50%;
    background: var(--logo-blue);
  }
</style>
</head>
<body>
<header class="banner">
  <div class="banner__backdrop" role="img" aria-label="Soft glowing bokeh of golden, coral, rose and white light"></div>
  <div class="banner__portrait" role="img" aria-label="Portrait of the founder in a light turquoise shirt, leaning in from the left"></div>

  <section class="invite">
    <p class="invite__kicker">together</p>
    <div class="invite__card">
      <p class="invite__line">we make tragic moments</p>
      <p class="invite__line invite__line--accent">magic moments</p>
    </div>
    <a class="invite__button" href="#join">Join us</a>
  </section>

  <div class="brand">
    <span class="brand__name">Tend Your Harvest</span>
    <span class="brand__person"><span class="brand__dot"></span>Marigold Thwaite</span>
  </div>
</header>
</body>
</html>
```